CBD Syrup Label 4" Wide, 2" Tall

I am looking for a fun modern supplement lab for a new CBD infused syrup. I have attached a few examples of some I like from other companies. Company name is Daveno. Logo is attached

Target Market(s)

Younger males

Font styles to use
Serif
Sans Serif

Colors

Designer to choose colors to be used in the design.

Requirements
Must have
• Logo centered. Each label a different color. Flavors will be descided later. Looking for colors or maybe fruit flavor ideas.

```html
<!DOCTYPE html>
<html lang="en">
<head>
<meta charset="utf-8">
<title>Daveno CBD Syrup Labels</title>
<link rel="stylesheet" href="https://fonts.googleapis.com/css2?family=Montserrat:wght@700;800;900&family=Bangers&display=swap">
<style>
  :root {
    --brand-green: #0f7a35;
    --brand-dark: #0b4f24;
    --ink: #1d1d1d;
    --paper: #ffffff;
    --pear-light: #e4f0a6;
    --pear: #a9c93a;
    --blueberry-light: #c9cdee;
    --blueberry: #3c3470;
    --watermelon-light: #f6c4d8;
    --watermelon: #e0507f;
    --cherry-light: #f7b3b0;
    --cherry: #d6202b;
    --peach-light: #fbd2a2;
    --peach: #ef7a2e;
  }
  * { box-sizing: border-box; margin: 0; padding: 0; }
  html, body {
    width: 1200px; height: 634px; overflow: hidden;
    background: var(--paper);
    font-family: "Montserrat", Arial, sans-serif;
  }
  .canvas { position: relative; width: 1200px; height: 634px; }
  .brand-header {
    position: absolute; top: 62px; left: 0; width: 100%;
    display: flex; justify-content: center; align-items: center; gap: 14px;
  }
  .brand-dot {
    width: 40px; height: 40px; border-radius: 50%;
    background: var(--brand-green);
  }
  .brand-name {
    font-weight: 800; font-size: 58px; color: var(--brand-green);
    letter-spacing: -1px; line-height: 1;
  }
  .label-row {
    position: absolute; top: 232px; left: 80px; width: 1040px;
    display: flex; justify-content: space-between;
  }
  .label {
    position: relative; width: 172px; height: 252px;
    background: var(--paper);
    border: 1px solid #e2e2e2;
    overflow: hidden;
    display: flex; flex-direction: column; align-items: center;
  }
  .label-brand {
    margin-top: 14px; display: flex; align-items: center; gap: 5px;
    font-weight: 800; font-size: 21px; color: var(--brand-green); line-height: 1;
  }
  .label-brand .mark {
    width: 14px; height: 14px; border-radius: 50%; background: var(--brand-green);
  }
  .label-splash {
    position: absolute; left: 0; right: 0; top: 58px; height: 150px;
  }
  .label-title {
    position: relative; margin-top: 14px; text-align: center; line-height: 0.9;
  }
  .label-title .cbd {
    display: block; font-weight: 900; font-size: 44px; color: var(--brand-green);
  }
  .label-title .syrup {
    display: block; font-weight: 900; font-size: 15px; color: var(--brand-dark); letter-spacing: 1px;
  }
  .label-fruit {
    position: relative; margin-top: 8px; width: 120px; height: 78px; border-radius: 40px;
  }
  .label-flavor {
    position: relative; margin-top: 10px;
    font-family: "Bangers", "Impact", sans-serif; font-size: 24px; letter-spacing: 1px;
    color: var(--ink); line-height: 1;
  }
  .label-volume {
    position: relative; margin-top: 5px; font-size: 9px; font-weight: 700; color: #444;
  }
  .pear .label-splash { background: radial-gradient(ellipse at 50% 60%, var(--pear) 0%, var(--pear-light) 60%, transparent 85%); }
  .pear .label-fruit { background: linear-gradient(135deg, #f4f8d8, var(--pear)); }
  .blueberry .label-splash { background: radial-gradient(ellipse at 50% 60%, #7e86cc 0%, var(--blueberry-light) 60%, transparent 85%); }
  .blueberry .label-fruit { background: linear-gradient(135deg, #6b63a8, var(--blueberry)); }
  .watermelon .label-splash { background: radial-gradient(ellipse at 50% 60%, var(--watermelon) 0%, var(--watermelon-light) 60%, transparent 85%); }
  .watermelon .label-fruit { background: linear-gradient(135deg, #ef5a5a, #4f9a3a); }
  .cherry .label-splash { background: radial-gradient(ellipse at 50% 60%, var(--cherry) 0%, var(--cherry-light) 60%, transparent 85%); }
  .cherry .label-fruit { background: linear-gradient(135deg, #e8434b, #9c0f1a); }
  .peach .label-splash { background: radial-gradient(ellipse at 50% 60%, var(--peach) 0%, var(--peach-light) 60%, transparent 85%); }
  .peach .label-fruit { background: linear-gradient(135deg, #fbd46b, #e8542a); }
</style>
</head>
<body>
<div class="canvas">
  <header class="brand-header">
    <span class="brand-dot"></span>
    <span class="brand-name">Daveno</span>
  </header>

  <section class="label-row">
    <article class="label pear">
      <div class="label-splash" role="img" aria-label="Green juice splash"></div>
      <div class="label-brand"><span class="mark"></span>Daveno</div>
      <h2 class="label-title"><span class="cbd">CBD</span><span class="syrup">SYRUP</span></h2>
      <div class="label-fruit" role="img" aria-label="Illustration of sliced pears with leaves"></div>
      <p class="label-flavor">PEAR</p>
      <p class="label-volume">1 fl oz/ 30ml</p>
    </article>

    <article class="label blueberry">
      <div class="label-splash" role="img" aria-label="Purple juice splash"></div>
      <div class="label-brand"><span class="mark"></span>Daveno</div>
      <h2 class="label-title"><span class="cbd">CBD</span><span class="syrup">SYRUP</span></h2>
      <div class="label-fruit" role="img" aria-label="Illustration of blueberries with leaves"></div>
      <p class="label-flavor">BLUEBERRY</p>
      <p class="label-volume">1 fl oz/ 30ml</p>
    </article>

    <article class="label watermelon">
      <div class="label-splash" role="img" aria-label="Pink juice splash"></div>
      <div class="label-brand"><span class="mark"></span>Daveno</div>
      <h2 class="label-title"><span class="cbd">CBD</span><span class="syrup">SYRUP</span></h2>
      <div class="label-fruit" role="img" aria-label="Illustration of watermelon slices"></div>
      <p class="label-flavor">WATERMELON</p>
      <p class="label-volume">1 fl oz/ 30ml</p>
    </article>

    <article class="label cherry">
      <div class="label-splash" role="img" aria-label="Red juice splash"></div>
      <div class="label-brand"><span class="mark"></span>Daveno</div>
      <h2 class="label-title"><span class="cbd">CBD</span><span class="syrup">SYRUP</span></h2>
      <div class="label-fruit" role="img" aria-label="Illustration of cherries with leaves"></div>
      <p class="label-flavor">CHERRY</p>
      <p class="label-volume">1 fl oz/ 30ml</p>
    </article>

    <article class="label peach">
      <div class="label-splash" role="img" aria-label="Orange juice splash"></div>
      <div class="label-brand"><span class="mark"></span>Daveno</div>
      <h2 class="label-title"><span class="cbd">CBD</span><span class="syrup">SYRUP</span></h2>
      <div class="label-fruit" role="img" aria-label="Illustration of sliced peaches"></div>
      <p class="label-flavor">PEACH</p>
      <p class="label-volume">1 fl oz/ 30ml</p>
    </article>
  </section>
</div>
</body>
</html>
```